BRAVO (Bright Regional Applied Vector Operations) Letter Head Design Project

Company Name: BRAVO (Bright Regional Applied Vector Operations) MFZ.
Office Address: Office No 718, Saffron Crest Block, Palmera Garden Quarter, Dubai, U.A.E
Company line of business:
1) Currently we have a POS solution for retail outlets like duty free shops, supermarkets, department stores etc... The solution is deployed in Harbourline Travel Retail on 350 POS and in Corniche Gate Travel Retail on 100 POS. So our main line of business is the deployment of this solution in retail outlets locally or regionally. We have already deployed the solution in India and Australia.
2) Integration of other third party POS systems with an online credit authorization netwotk in the UAE. This will enable POS applications to connect directly to the acquiring banks without needing an EFT terminal like Paxomat or Tallyrex. The credit card payment is completed at the POS.
3) Other solutions that are targeting retail outlets like mobile POS, queue busting solutions, stock taking solutions using hand held devices, transaction capture systems, etc...
4) Other IT services like support of call center solutions from Bluegrove Systems and development of new solutions as per customer requirements.
We need a letter head design for the company. We don't have any specific requirements in mind and we prefer to leave it up to the designers to come up with creative designs that will not be limited by any guidelines.
Updates
I have just uploaded all the files I received from my company logo designer. Please review and let me know if you need anything else. .
Dear All,
I have received very nice designs and I thank you for all the hard work you have put so far. I would like the letter head to have all the following company details:
Office Address: Office No 718, Saffron Crest Block, MFZ, Dubai UAE
P.O.Box: 58316 Dubai UAE
Tel Number:+971-4-5817730
Fax Number::+971-4-5817731
Website:www.bravomfz.ae
I would also like to represent the company details as a QRCode somewhere on the page, probably next to the company details if possible (as a trial).
In case you have included a butterfly in the middle of the page as part of your design, I prefer that it doesn't include any colors as colors might make reading the text on the page more difficult.
I don't want to have too many butterflies on the page. 2 are more than enough.
Can you also include a design for the continuation pages?
Thank you in advance and I look forward to receiving your creative designs.
Regards
Samir Odeyra

```html
<!DOCTYPE html>
<html lang="en">
<head>
<meta charset="utf-8">
<title>BRAVO Letterhead and Continuation Page</title>
<link rel="stylesheet" href="https://fonts.googleapis.com/css2?family=PT+Sans:wght@400;700&display=swap">
<style>
  :root {
    --backdrop: #a8832a;
    --paper: #ffffff;
    --ink: #1a1a1a;
    --ink-soft: #3a3a3a;
    --mark: #2c7fc3;
    --watermark: #eef1f4;
    --icon: #3a9bd8;
    --band-blue: #2a8fd0;
    --band-yellow: #f2e45a;
    --band-green: #9cc85a;
    --band-red: #e2545e;
  }
  * { margin: 0; padding: 0; box-sizing: border-box; }
  html, body { width: 1200px; height: 795px; overflow: hidden; }
  body {
    background: var(--backdrop);
    font-family: "PT Sans", Arial, sans-serif;
    color: var(--ink);
    position: relative;
  }
  .sheet {
    position: absolute;
    top: 50px;
    width: 531px;
    height: 685px;
    background: var(--paper);
    overflow: hidden;
  }
  .sheet--first { left: 13px; }
  .sheet--continuation { left: 611px; }

  .brand {
    position: absolute;
    left: 32px;
    top: 36px;
    display: flex;
    align-items: center;
    gap: 14px;
  }
  .brand__dot {
    width: 46px; height: 46px;
    border-radius: 50%;
    background: var(--mark);
  }
  .brand__name {
    font-size: 44px;
    font-weight: 400;
    letter-spacing: 1px;
    line-height: 1;
    color: var(--ink);
  }

  .watermark {
    position: absolute;
    left: 0; right: 0;
    top: 320px;
    text-align: center;
    font-size: 120px;
    font-weight: 400;
    letter-spacing: 4px;
    color: var(--watermark);
    line-height: 1;
  }

  .contact {
    font-size: 8px;
    line-height: 1.3;
    color: var(--ink-soft);
    list-style: none;
    white-space: nowrap;
  }
  .contact li { display: flex; align-items: center; gap: 3px; }
  .contact span { display: inline-flex; align-items: center; gap: 3px; }
  .contact svg { width: 7px; height: 7px; flex: none; }
  .contact--header {
    position: absolute;
    left: 384px;
    top: 24px;
  }
  .contact--header .contact__address { display: block; margin-bottom: 4px; }
  .contact--footer {
    position: absolute;
    left: 15px;
    top: 636px;
  }
  .contact__row { gap: 10px !important; margin-top: 5px; }

  .corner-band {
    position: absolute;
    inset: 0;
    width: 100%;
    height: 100%;
  }
</style>
</head>
<body>

<section class="sheet sheet--first" aria-label="Letterhead first page">
  <div class="brand">
    <span class="brand__dot"></span>
    <span class="brand__name">BRAVO</span>
  </div>

  <ul class="contact contact--header">
    <li class="contact__address">Office No 718, Saffron Crest Block,<br>Palmera Garden Quarter, Dubai, U.A.E</li>
    <li><svg viewBox="0 0 10 10"><path fill="var(--icon)" d="M2 1l2 2-1 1.5c.6 1.2 1.3 1.9 2.5 2.5L7 6l2 2-1.5 1.5C4.5 9 1 5.5.5 2z"/></svg>123-456-7890</li>
    <li><svg viewBox="0 0 10 10"><rect fill="var(--icon)" x="1" y="4" width="8" height="5" rx="1"/><rect fill="var(--icon)" x="3" y="1" width="4" height="3"/></svg>123-456-7890</li>
    <li><svg viewBox="0 0 10 10"><circle fill="var(--icon)" cx="5" cy="5" r="5"/></svg>bravo@email.com</li>
    <li><svg viewBox="0 0 10 10"><circle fill="var(--icon)" cx="5" cy="5" r="5"/></svg>www.website.com</li>
  </ul>

  <div class="watermark" aria-hidden="true">BRAVO</div>

  <svg class="corner-band" viewBox="0 0 531 685" preserveAspectRatio="none" role="img" aria-label="Decorative multicoloured corner band">
    <defs>
      <linearGradient id="band-first" x1="0.7" y1="0" x2="0" y2="1">
        <stop offset="0" stop-color="var(--band-blue)"/>
        <stop offset="0.45" stop-color="var(--band-yellow)"/>
        <stop offset="0.7" stop-color="var(--band-green)"/>
        <stop offset="1" stop-color="var(--band-red)"/>
      </linearGradient>
    </defs>
    <polygon fill="url(#band-first)" points="0,566 326,685 0,685"/>
  </svg>
</section>

<section class="sheet sheet--continuation" aria-label="Letterhead continuation page">
  <div class="brand">
    <span class="brand__dot"></span>
    <span class="brand__name">BRAVO</span>
  </div>

  <div class="watermark" aria-hidden="true">BRAVO</div>

  <svg class="corner-band" viewBox="0 0 531 685" preserveAspectRatio="none" role="img" aria-label="Decorative multicoloured corner band">
    <defs>
      <linearGradient id="band-continuation" x1="0.3" y1="0" x2="1" y2="1">
        <stop offset="0" stop-color="var(--band-blue)"/>
        <stop offset="0.45" stop-color="var(--band-yellow)"/>
        <stop offset="0.7" stop-color="var(--band-green)"/>
        <stop offset="1" stop-color="var(--band-red)"/>
      </linearGradient>
    </defs>
    <polygon fill="url(#band-continuation)" points="165,685 531,604 531,685"/>
  </svg>

  <ul class="contact contact--footer">
    <li>Office No 718, Saffron Crest Block, Palmera Garden Quarter, Dubai, U.A.E</li>
    <li class="contact__row">
      <span><svg viewBox="0 0 10 10"><path fill="var(--icon)" d="M2 1l2 2-1 1.5c.6 1.2 1.3 1.9 2.5 2.5L7 6l2 2-1.5 1.5C4.5 9 1 5.5.5 2z"/></svg>123-456-7890</span>
      <span><svg viewBox="0 0 10 10"><rect fill="var(--icon)" x="1" y="4" width="8" height="5" rx="1"/><rect fill="var(--icon)" x="3" y="1" width="4" height="3"/></svg>123-456-7890</span>
    </li>
    <li class="contact__row">
      <span><svg viewBox="0 0 10 10"><circle fill="var(--icon)" cx="5" cy="5" r="5"/></svg>bravo@email.com</span>
      <span><svg viewBox="0 0 10 10"><circle fill="var(--icon)" cx="5" cy="5" r="5"/></svg>www.website.com</span>
    </li>
  </ul>
</section>

</body>
</html>
```